A Hair, Beauty and Nails Wholesalers Needs a Business Card Design

We need a business card design for our company which is being passed from parents to daughter, so we wont to re-launch the company with an updated, modern, sophisticated, elegant, chic and fresh look which still incorporates the original colour scheme of Hot Pink, Dark Grey and White. The original logo which is attached can be used on the card but we would like to see some designs with the logo and some without, as we have not yet decided if we want the logo on the card. The name of our company is 'Velmora Supplies' and the name of our website is VelmoraGlowandPolish.example.au. We specialise in supplying a massive range of Hair, Beauty and Nail products to the industry. We are based in QLD, Australia but ship many orders via our website all across Australia.

```html
<!DOCTYPE html>
<html lang="en">
<head>
<meta charset="utf-8">
<title>Velmora Supplies – Business Card</title>
<link rel="stylesheet" href="https://fonts.googleapis.com/css2?family=Open+Sans:wdth,wght@75..100,400&family=Italianno&display=swap">
<style>
  :root {
    --bg-light: #cfccc9;
    --bg-mid: #6e6c6b;
    --bg-dark: #1e1e1e;
    --ink: #ffffff;
    --pink-hot: #ff7fc8;
    --pink-mid: #d65a9a;
    --pink-deep: #8e3a68;
  }
  html, body {
    margin: 0;
    padding: 0;
    width: 1200px;
    height: 725px;
    overflow: hidden;
    background: var(--bg-dark);
  }
  .card {
    position: relative;
    width: 1200px;
    height: 725px;
    overflow: hidden;
    background: radial-gradient(ellipse 900px 700px at 380px 300px,
      var(--bg-light) 0%, #9d9a98 30%, var(--bg-mid) 55%, #333 80%, var(--bg-dark) 100%);
    font-family: "Open Sans", Arial, sans-serif;
    color: var(--ink);
  }
  .bloom {
    position: absolute;
    left: 0;
    top: 0;
    width: 540px;
    height: 725px;
  }
  .brand-name {
    position: absolute;
    left: 572px;
    top: 12px;
    margin: 0;
    font-family: "Italianno", cursive;
    font-weight: 400;
    font-size: 118px;
    line-height: 1;
    color: var(--ink);
    white-space: nowrap;
  }
  .divider {
    position: absolute;
    left: 536px;
    top: 268px;
    width: 2px;
    height: 390px;
    background: var(--ink);
  }
  .contact-icon {
    position: absolute;
    fill: var(--ink);
  }
  .contact-text {
    position: absolute;
    left: 640px;
    margin: 0;
    font-size: 34px;
    font-weight: 400;
    line-height: 1.2;
    white-space: nowrap;
  }
  .contact-text.online {
    font-size: 32px;
    font-stretch: 80%;
    letter-spacing: -0.2px;
  }
  .person-name { top: 317px; }
  .person-role {
    position: absolute;
    left: 638px;
    top: 346px;
    margin: 0;
    font-size: 19px;
    white-space: nowrap;
  }
  .phone { top: 383px; }
  .email { top: 448px; }
  .web { top: 516px; }
  .address { top: 590px; line-height: 1.42; }
</style>
</head>
<body>
<div class="card">
  <svg class="bloom" role="img" aria-label="Large stylised pink flower with layered pointed petals radiating from a white centre" viewBox="0 0 540 725">
    <defs>
      <radialGradient id="bloomFill" cx="40" cy="340" r="500" gradientUnits="userSpaceOnUse">
        <stop offset="0" stop-color="#ffffff"/>
        <stop offset="0.18" stop-color="#ffc6e6"/>
        <stop offset="0.4" stop-color="#ff7fc8"/>
        <stop offset="0.7" stop-color="#d65a9a"/>
        <stop offset="1" stop-color="#8e3a68"/>
      </radialGradient>
    </defs>
    <ellipse cx="40" cy="350" rx="490" ry="380" fill="url(#bloomFill)"/>
  </svg>

  <h1 class="brand-name">Velmora Supplies</h1>

  <div class="divider"></div>

  <svg class="contact-icon" style="left:544px;top:320px" width="42" height="40" viewBox="0 0 42 40" aria-hidden="true">
    <circle cx="21" cy="11" r="10"/>
    <path d="M0 40 C0 28 10 23 21 23 C32 23 42 28 42 40 Z"/>
  </svg>
  <p class="contact-text person-name">Marisa Kellaway</p>
  <p class="person-role">(Manager)</p>

  <svg class="contact-icon" style="left:555px;top:393px" width="16" height="20" viewBox="0 0 16 20" aria-hidden="true">
    <path d="M3 1 L6 1 L7 6 L5 7 C5.5 10 7 13 9 14.5 L11 13 L15 16 L14 19 C7 19 1 11 1 3 Z"/>
  </svg>
  <p class="contact-text phone">(07) 5550 0192</p>

  <svg class="contact-icon" style="left:554px;top:462px" width="22" height="16" viewBox="0 0 22 16" aria-hidden="true">
    <path d="M1 1 H21 V15 H1 Z M3 3 V13 H19 V3 L11 9 Z M4 3 L11 8 L18 3 Z" fill-rule="evenodd"/>
  </svg>
  <p class="contact-text online email">admin@velmoraglowandpolish.example.au</p>

  <svg class="contact-icon" style="left:555px;top:528px" width="24" height="24" viewBox="0 0 24 24" aria-hidden="true">
    <path d="M10 1 A9 9 0 1 0 10 19 A9 9 0 1 0 10 1 Z M10 3 A7 7 0 1 1 10 17 A7 7 0 1 1 10 3 Z" fill-rule="evenodd"/>
    <rect x="3" y="9" width="14" height="2"/>
    <rect x="9" y="2" width="2" height="16"/>
    <path d="M13 12 L23 16 L19 17 L22 21 L20 23 L17 19 L15 22 Z"/>
  </svg>
  <p class="contact-text online web">www.velmoraglowandpolish.example.au</p>

  <svg class="contact-icon" style="left:556px;top:601px" width="22" height="20" viewBox="0 0 22 20" aria-hidden="true">
    <path d="M11 1 L21 10 L18 10 L18 19 L13 19 L13 13 L9 13 L9 19 L4 19 L4 10 L1 10 Z"/>
  </svg>
  <p class="contact-text address">58 Larkin Street<br>BRAMWELL, QLD, 4712</p>
</div>
</body>
</html>
```